Book Title: The Harvest Lantern. Author Name: Marisa Thornbury

We are needing a cover, spine and back cover design for a poetry book that we are publishing called The Harvest Lantern. We are looking for an elegant, and simplistic design with a very natural, dynamic and powerful impact.

Design Idea #1 - Shiva Conch Shell with a pink or black background. See Colin Vesey Image attached for design inspiration. Simple and dynamic .
Title and Author name created in same style as the attached Colin Vesey's Ledgers and Lanterns image.

Design Idea #2 - Image of cauldron on (see cauldrons attached for ideas) black background.
See Colin Vesey Image attached for design inspiration. Simple and dynamic Title and Author name created in same style as the attached Colin Vesey's Ledgers and Lanterns image

Design Idea #3 - Image of Tree of Life (see attached images for idea of what we are looking for) Would like to see on plain white, green, black and green background.

Target Market(s)

Spiritual Women, healers, visionaries,Goddess'

Requirements
Must have
• Please see project descriptions for specific design concepts we are looking for. Please include the authors name: Marisa Thornbury on front, spine and back cover of the book

```html
<!DOCTYPE html>
<html lang="en">
<head>
<meta charset="utf-8">
<title>The Harvest Lantern — Spine and Front Cover</title>
<link rel="stylesheet" href="https://fonts.googleapis.com/css2?family=Crimson+Pro:wght@400;500;600&display=swap">
<style>
  :root {
    --page-bg: #ffffff;
    --cover-black: #000000;
    --cover-sheen: #262626;
    --spine-edge: #1a1a1a;
    --title-pink: #f4d3e2;
    --shell-light: #e6ebe5;
    --shell-mid: #c8cdc3;
    --shell-warm: #cdb49a;
  }
  * { margin: 0; padding: 0; box-sizing: border-box; }
  html, body {
    width: 1200px;
    height: 1200px;
    overflow: hidden;
    background: var(--page-bg);
  }
  .canvas {
    position: relative;
    width: 1200px;
    height: 1200px;
  }
  .book {
    position: absolute;
    left: 258px;
    top: 150px;
    width: 684px;
    height: 900px;
    display: flex;
    color: var(--title-pink);
    font-family: "Crimson Pro", "Times New Roman", serif;
  }
  .spine {
    position: relative;
    width: 64px;
    height: 100%;
    background: var(--cover-black);
    border-right: 2px solid var(--spine-edge);
  }
  .spine-title,
  .spine-author {
    position: absolute;
    left: 50%;
    writing-mode: vertical-rl;
    transform: translateX(-50%);
    white-space: nowrap;
  }
  .spine-title {
    top: 68px;
    font-weight: 500;
    font-size: 19px;
    letter-spacing: 0.16em;
    text-transform: uppercase;
  }
  .spine-author {
    top: 620px;
    font-weight: 600;
    font-size: 19px;
    letter-spacing: 0.1em;
  }
  .front-cover {
    position: relative;
    width: 620px;
    height: 100%;
    background: linear-gradient(135deg, var(--cover-sheen) 0%, var(--cover-black) 32%, var(--cover-black) 100%);
    text-align: center;
  }
  .book-title {
    position: absolute;
    top: 96px;
    left: 0;
    right: 0;
    font-weight: 400;
    font-size: 44px;
    line-height: 86px;
    letter-spacing: 0.2em;
    padding-left: 0.2em;
    text-transform: uppercase;
  }
  .cover-art {
    position: absolute;
    left: 50%;
    top: 395px;
    width: 160px;
    height: 290px;
    transform: translateX(-50%);
    border-radius: 50%;
    background: radial-gradient(ellipse at 50% 60%, var(--shell-light) 0%, var(--shell-mid) 35%, var(--shell-warm) 50%, rgba(0,0,0,0) 70%);
  }
  .author-name {
    position: absolute;
    top: 835px;
    top: 730px;
    left: 0;
    right: 0;
    font-weight: 500;
    font-size: 52px;
    line-height: 80px;
    letter-spacing: 0.16em;
    padding-left: 0.16em;
  }
</style>
</head>
<body>
  <main class="canvas">
    <article class="book">
      <aside class="spine">
        <span class="spine-title">The Harvest Lantern</span>
        <span class="spine-author">Marisa Thornbury</span>
      </aside>
      <section class="front-cover">
        <h1 class="book-title">The Harvest<br>Lantern</h1>
        <div class="cover-art" role="img" aria-label="Photograph of a pale white conch shell, point upward, on black"></div>
        <p class="author-name">Marisa<br>Thornbury</p>
      </section>
    </article>
  </main>
</body>
</html>
```